Business card for biotech sales agent

I need a logo and business card designed for my company Telmora. We work in partnership with Kivex Group. Telmora have developed advanced biotech. Their hand sanitiser is alcohol free and works for 24 hours on skin, even with regular hand washing. The surface sanitiser works for up to 30 days on surfaces and fabrics. Its food-safe, it's non-toxic, safe for animals and humans. The products have a very wide variety of applications: everything from agri-business, hotels, hospitality, schools, child and baby care, transport, meat processing etc.<br/>I would like my design to use blues or green-blues and communicate a bit of nano-tech but also trust and safety.<br/>I would also use the Telmora logo on my card next to 'sales & distribution agent'

Target Market(s)

B2B, selling to FMCG and large companies such as airlines

Industry/Entity Type

Biotechnology

Contact Information for Business Card

Joan Pelling
Director

Phone: +64 22 519 3064
Email: joan@telmora.co
www.telmora.co
14 Callery St, Westhaven, Auckland, New Zealand 1047

Font styles to use
Sans Serif

Colors
3276b5
33b8a4
34a7d8
3176b5
ffffff

Requirements
Must have
• Not be too busy, clean space is good
• A logo styling to the word Telmora
Nice to have
• A little bit of a bio-tech image as a screen perhaps

```html
<!DOCTYPE html>
<html lang="en">
<head>
<meta charset="utf-8">
<title>Telmora – Sales &amp; Distribution Agent business card</title>
<link rel="stylesheet" href="https://fonts.googleapis.com/css2?family=Roboto:wght@300;400;500;700&display=swap">
<style>
  :root {
    --backdrop: #e9ebec;
    --card: #1f3550;
    --card-deep: #1b2f47;
    --accent: #33b8a4;
    --accent-blue: #34a7d8;
    --brand-blue: #3176b5;
    --ink: #ffffff;
    --ink-soft: #dfe8f0;
    --rule: #6d86a0;
    --emboss: #3e5877;
    --emboss-light: #4d6a8c;
  }
  * { box-sizing: border-box; margin: 0; padding: 0; }
  html, body {
    width: 1200px; height: 801px; overflow: hidden;
    background: var(--backdrop);
    font-family: "Roboto", Arial, sans-serif;
  }
  .sheet {
    position: relative; width: 1200px; height: 801px;
    display: flex; align-items: center; justify-content: center; gap: 60px;
  }
  .card {
    position: relative; width: 525px; height: 300px;
    background: var(--card);
    border-bottom: 4px solid var(--accent);
    border-left: 2px solid var(--accent);
    box-shadow: 0 12px 30px rgba(0,0,0,.22);
  }

  /* Front */
  .card-front .brand {
    position: absolute; left: 40px; top: 116px;
    display: flex; align-items: center; gap: 10px;
  }
  .brand-dot {
    width: 18px; height: 18px; border-radius: 50%;
    background: var(--accent);
  }
  .brand-name {
    font-weight: 700; font-size: 44px; line-height: 1;
    color: var(--ink); letter-spacing: -0.5px;
  }
  .card-front .tagline {
    position: absolute; left: 68px; top: 168px;
    font-size: 9px; font-weight: 500; letter-spacing: 1.5px;
    color: var(--accent-blue); text-transform: uppercase;
  }
  .divider {
    position: absolute; left: 300px; top: 52px;
    width: 1px; height: 196px; background: var(--rule);
  }
  .contact {
    position: absolute; left: 322px; top: 56px; right: 14px;
    color: var(--ink-soft); font-size: 12px; line-height: 1.35;
  }
  .contact-name { color: var(--accent); font-size: 19px; font-weight: 500; }
  .contact-role { color: var(--ink); font-size: 15px; font-weight: 300; margin-bottom: 12px; }
  .contact-address { font-weight: 300; margin-bottom: 12px; }
  .contact-list { list-style: none; font-weight: 300; }
  .contact-list li { display: flex; align-items: center; gap: 9px; margin-bottom: 4px; }
  .contact-list svg { width: 12px; height: 12px; flex: none; }

  /* Back */
  .card-back { background: var(--card-deep); }
  .card-back .brand-large {
    position: absolute; left: 0; right: 0; top: 92px;
    text-align: center;
    font-weight: 700; font-size: 96px; line-height: 1;
    color: var(--emboss-light);
    letter-spacing: -1px;
  }
  .card-back .tagline-large {
    position: absolute; left: 0; right: 0; top: 200px;
    text-align: center;
    font-size: 14px; font-weight: 500; letter-spacing: 3px;
    color: var(--emboss); text-transform: uppercase;
  }
</style>
</head>
<body>
<main class="sheet">
  <section class="card card-front" aria-label="Business card front">
    <div class="brand">
      <span class="brand-dot"></span>
      <span class="brand-name">Telmora</span>
    </div>
    <p class="tagline">Sales &amp; Distribution Agent</p>
    <div class="divider"></div>
    <div class="contact">
      <p class="contact-name">Joan Pelling</p>
      <p class="contact-role">Director</p>
      <p class="contact-address">14 Callery St, Westhaven,<br>Auckland, New Zealand 1047</p>
      <ul class="contact-list">
        <li>
          <svg viewBox="0 0 12 12" aria-hidden="true"><path d="M2.5 1h2l1 2.6-1.3 1a6 6 0 0 0 3.2 3.2l1-1.3L11 7.5v2c0 .8-.7 1.5-1.5 1.4C5 10.5 1.5 7 1.1 2.5 1 1.7 1.7 1 2.5 1z" fill="var(--accent)"/></svg>
          +64 22 519 3064
        </li>
        <li>
          <svg viewBox="0 0 12 12" aria-hidden="true"><rect x="1" y="2.5" width="10" height="7" fill="none" stroke="var(--accent)" stroke-width="1.2"/><path d="M1 2.5l5 4 5-4" fill="none" stroke="var(--accent)" stroke-width="1.2"/></svg>
          joan@telmora.co
        </li>
        <li>
          <svg viewBox="0 0 12 12" aria-hidden="true"><circle cx="6" cy="6" r="5" fill="var(--accent)"/><path d="M1 6h10M6 1c-2.5 2.8-2.5 7.2 0 10M6 1c2.5 2.8 2.5 7.2 0 10" stroke="var(--card)" stroke-width=".8" fill="none"/></svg>
          www.telmora.co
        </li>
      </ul>
    </div>
  </section>

  <section class="card card-back" aria-label="Business card back">
    <p class="brand-large">Telmora</p>
    <p class="tagline-large">Sales &amp; Distribution Agent</p>
  </section>
</main>
</body>
</html>
```